Vibrational sessions for Healing

I am looking for a business card that is unique that sends a message to open minded folk that vibrational healing is paramount to their life journey and if they are open to this idea it can move mountains for them! All they have to have is a belief! IT is as simple as that!
Meadow Lantern is the company based in Western Australia, and as the energy that we are working with is everywhere, it is universal, so to speak!
The design we would like to see is of light shades of rainbow colours radiating light and energy so whatever you think is appropriate to send the message that if you want to move on in you life in a down to earth fashion, then this is the way for folk to find themselves! Something completely different and out of the ordinary and affordable to most, quirky in nature, but completely out of this world idea that will hit the masses by storm!
A website is being developed as we speak, so a new method of healing will be upon us very soon in an unusual fasion, so to speak!
Looking forward to your wonderful bright ideas so we an get started on this venture to enlighten many folk that are on the brink of making a truthful life for themselves.
Warm Regards,
Ruth

Reason: Hi there, I am new to this game and as this is my first time advertising with ArtHuddle, I was unaware of the time it takes to submit replies and answers to the designers. As I posted the add early in the week, I feel that those first 2 days were just acknowledging designers and sending off extra information for the deign of the card. I would appreciate an extension of time. Thank you. Ruth

Business

Vibrational Healing, Ruth Tallowby, Coralbay WA 6537, Practitioner

Abstract Logo
• As this is energy we are talking about, a design that is wispy with a hint of something happening on the card, pastel shades but can be a bold colour somewhere to be a feature but not to striking. Also a vague hint of a clothed body (male or female or both, in dress or suit whatever, casual is fine, in an abstract form) that is just distinguishable in the background.
I would like a design that makes people look twice at the design and then they can read into what can actually happen for themselves.
I hope all this makes sense. Any questions, please email me for clarification.Thank you all for being part of the project to get this underway! This will happen!

```html
<!DOCTYPE html>
<html lang="en">
<head>
<meta charset="utf-8">
<title>Meadow Lantern – Business Card</title>
<link rel="stylesheet" href="https://fonts.googleapis.com/css2?family=Roboto:wght@300;400;500&family=Roboto+Condensed:wght@400;700&display=swap">
<style>
  :root {
    --backdrop: #ecebe8;
    --card: #ffffff;
    --ink: #1d1d1d;
    --ink-soft: #333333;
    --mark: #8fc9e6;
    --red: #f3897f;
    --orange: #f7b877;
    --yellow: #f4e98a;
    --green: #a3d898;
    --teal: #8dd3d5;
    --blue: #93b9e6;
  }
  * { box-sizing: border-box; margin: 0; padding: 0; }
  html, body { width: 1200px; height: 945px; overflow: hidden; }
  body { background: var(--backdrop); position: relative; }

  .card {
    position: absolute;
    left: 365px; top: 42px;
    width: 470px; height: 860px;
    background: var(--card);
    box-shadow: 0 6px 24px rgba(0,0,0,0.12);
    overflow: hidden;
    text-align: center;
    color: var(--ink);
  }
  .brand-mark {
    position: absolute;
    left: 50%; top: 40px;
    width: 150px; height: 150px;
    margin-left: -75px;
    border-radius: 50%;
    background: var(--mark);
  }
  .brand-name {
    position: absolute; left: 0; right: 0; top: 222px;
    font-family: "Roboto", sans-serif;
    font-weight: 400;
    font-size: 43px;
    letter-spacing: -0.5px;
  }
  .service {
    position: absolute; left: 0; right: 0; top: 276px;
    font-family: "Roboto", sans-serif;
    font-weight: 300;
    font-size: 43px;
    letter-spacing: -0.5px;
  }
  .practitioner-name {
    position: absolute; left: 0; right: 0; top: 350px;
    font-family: "Roboto", sans-serif;
    font-weight: 500;
    font-size: 31px;
  }
  .contact {
    position: absolute; left: 0; right: 0; top: 398px;
    font-family: "Roboto Condensed", sans-serif;
    font-size: 20px;
    line-height: 31px;
    color: var(--ink-soft);
    list-style: none;
  }
  .contact b { font-weight: 700; color: var(--ink); }

  .energy-area {
    position: absolute; left: 0; right: 0; bottom: 0;
    height: 270px;
    background: linear-gradient(90deg, var(--red), var(--orange) 22%, var(--yellow) 42%, var(--green) 58%, var(--teal) 78%, var(--blue));
  }
</style>
</head>
<body>
  <article class="card">
    <div class="brand-mark"></div>
    <h1 class="brand-name">Meadow Lantern</h1>
    <p class="service">Vibrational Healing</p>
    <h2 class="practitioner-name">Ruth Tallowby</h2>
    <ul class="contact">
      <li>Coralbay WA 6537, Practitioner</li>
      <li><b>mobile:</b> 0412558930</li>
      <li><b>email:</b> ruth@meadowlantern.net.au</li>
      <li><b>website:</b> www.meadowlantern.net.au</li>
      <li><b>location:</b> Perth, Western Australia</li>
    </ul>
    <div class="energy-area" role="img" aria-label="Decorative rainbow pattern radiating up from the bottom of the card"></div>
  </article>
</body>
</html>
```